Design some Business Cards & Stationary for KWT

I need a design mockup for a company's business cards and their letterhead. I've attached the logo and listed what company info I want on the cards and letterhead below. Thanks.

Name
Job Title
Address
Office #
Mobile #
Email
Website

```html
<!DOCTYPE html>
<html lang="en">
<head>
<meta charset="UTF-8">
<title>KWT Business Card</title>
<link href="https://fonts.googleapis.com/css2?family=Montserrat:wght@500;700;800&display=swap" rel="stylesheet">
<style>
  :root {
    --navy: #1f4584;
    --navy-deep: #1b3d78;
    --bright-blue: #3f8ee0;
    --paper: #f7f7f5;
    --ink: #1f3f78;
    --stage: #e4e6ea;
  }
  * { margin: 0; padding: 0; box-sizing: border-box; }
  html, body { width: 1200px; height: 872px; overflow: hidden; }
  body {
    background: var(--stage);
    font-family: "Montserrat", Arial, sans-serif;
    position: relative;
  }
  .card {
    position: absolute;
    top: 138px;
    width: 340px;
    height: 596px;
    border-radius: 3px;
    overflow: hidden;
    box-shadow: 0 6px 18px rgba(0,0,0,0.12);
  }
  .card-front { left: 190px; background: var(--paper); }
  .card-back { left: 670px; background: var(--navy); }

  .brand { position: absolute; color: var(--navy); font-weight: 800; }
  .card-front .brand { left: 34px; top: 42px; }
  .brand-initials { display: block; font-size: 46px; line-height: 1; letter-spacing: 1px; }
  .brand-name {
    display: block; font-size: 10px; letter-spacing: 2.4px;
    text-transform: uppercase; margin-top: 4px; font-weight: 800;
  }

  .person { position: absolute; left: 34px; top: 138px; color: var(--ink); }
  .person-name { font-size: 24px; font-weight: 700; line-height: 1; }
  .person-title { font-size: 9px; font-weight: 500; margin-top: 5px; }

  .contacts {
    position: absolute; left: 34px; top: 400px;
    list-style: none; color: var(--ink);
    font-size: 10px; font-weight: 700; line-height: 17px;
  }
  .contacts span { font-weight: 500; }

  .band {
    position: absolute; left: 0; bottom: 0; width: 100%; height: 82px;
    background: var(--navy-deep);
    color: #fff; font-size: 10px; font-weight: 700;
    display: flex; align-items: center; padding-left: 34px;
  }
  .band span { font-weight: 500; margin-left: 4px; }
  .band-rule {
    position: absolute; left: 0; bottom: 92px; width: 100%; height: 4px;
    background: var(--navy-deep);
  }

  .card-back .brand {
    left: 0; right: 0; top: 236px; text-align: center; color: var(--bright-blue);
  }
  .card-back .brand-initials { font-size: 96px; }
  .card-back .brand-name { font-size: 15px; letter-spacing: 3.5px; margin-top: 8px; }
</style>
</head>
<body>
  <section class="card card-front">
    <div class="brand">
      <span class="brand-initials">KWT</span>
      <span class="brand-name">Kenwick Works Trading</span>
    </div>
    <div class="person">
      <p class="person-name">john doe</p>
      <p class="person-title">branding manager</p>
    </div>
    <ul class="contacts">
      <li>address: <span>4120 harbor road, bayview</span></li>
      <li>email: <span>your email here@.com</span></li>
      <li>mobile: <span>(000) 000-0000</span></li>
      <li>office: <span>(000) 000-0000</span></li>
    </ul>
    <div class="band-rule"></div>
    <div class="band">website: <span>your website here.com</span></div>
  </section>

  <section class="card card-back">
    <div class="brand">
      <span class="brand-initials">KWT</span>
      <span class="brand-name">Kenwick Works Trading</span>
    </div>
  </section>
</body>
</html>
```